Ridgeline Sawcutting, Inc. Business Card

Create a business card that is eye catching and based around concrete sawcutting. I've attached our current business card and logo for reference. We like aspects of the current business card, but it is starting to feel very loud and lost. We would like something that is still fun but is more modern and streamlined.

```html
<!DOCTYPE html>
<html lang="en">
<head>
<meta charset="utf-8">
<title>Ridgeline Sawcutting, Inc. Business Card</title>
<link href="https://fonts.googleapis.com/css2?family=Montserrat:wght@400;500;600;700&display=swap" rel="stylesheet">
<style>
  :root {
    --bg: #d9d9d7;
    --navy: #1f2955;
    --red: #d3202b;
    --gold: #f5c518;
    --white: #ffffff;
    --rule: #b01e2a;
    --muted: #8a92b4;
  }
  * { box-sizing: border-box; margin: 0; padding: 0; }
  html, body { width: 1200px; height: 801px; overflow: hidden; }
  body {
    background: var(--bg);
    font-family: "Montserrat", Arial, sans-serif;
    display: flex;
    align-items: center;
    justify-content: center;
    gap: 40px;
  }
  .card {
    position: relative;
    width: 540px;
    height: 309px;
    background: var(--navy);
    border-bottom: 4px solid var(--gold);
    border-right: 4px solid var(--gold);
    color: var(--white);
    box-shadow: 0 10px 24px rgba(0,0,0,0.25);
  }
  .brand {
    display: flex;
    align-items: center;
    gap: 10px;
    font-weight: 600;
    color: var(--white);
    letter-spacing: 0.04em;
    text-transform: uppercase;
  }
  .brand-dot {
    border-radius: 50%;
    background: var(--red);
    flex: none;
  }

  /* front */
  .card-front .brand { position: absolute; top: 48px; right: 40px; font-size: 15px; }
  .card-front .brand-dot { width: 22px; height: 22px; }
  .identity { position: absolute; left: 36px; top: 150px; }
  .identity .name {
    color: var(--red);
    font-weight: 700;
    font-size: 24px;
    letter-spacing: 0.02em;
    text-transform: uppercase;
    line-height: 1.05;
  }
  .identity .title { font-size: 13px; font-weight: 400; margin-top: 3px; }
  .rule { position: absolute; left: 36px; right: 30px; top: 206px; height: 1px; background: var(--rule); }
  .contacts {
    position: absolute; left: 36px; right: 20px; top: 220px;
    display: flex; align-items: stretch; gap: 14px;
    font-size: 10.5px; line-height: 1.75;
  }
  .contact-group { display: flex; flex-direction: column; }
  .contact-divider { width: 1px; background: var(--muted); margin: 4px 0; }
  .contact-row { display: flex; align-items: center; gap: 5px; white-space: nowrap; }
  .contact-row svg { width: 9px; height: 9px; flex: none; }

  /* back */
  .card-back .brand {
    position: absolute; top: 86px; left: 0; right: 0;
    justify-content: center; font-size: 20px;
  }
  .card-back .brand-dot { width: 28px; height: 28px; }
  .hotline {
    position: absolute; top: 196px; left: 0; right: 0; text-align: center;
    color: var(--gold); font-weight: 700; font-size: 16px; letter-spacing: 0.03em;
  }
  .services {
    position: absolute; top: 232px; left: 0; right: 0; text-align: center;
    font-size: 12px; font-weight: 500; letter-spacing: 0.03em;
  }
  .services .sep { color: var(--gold); margin: 0 5px; }
</style>
</head>
<body>
  <section class="card card-front">
    <div class="brand"><span class="brand-dot"></span>Ridgeline Sawcutting</div>
    <div class="identity">
      <div class="name">Dana Moretti</div>
      <div class="title">Owner/CEO</div>
    </div>
    <div class="rule"></div>
    <div class="contacts">
      <div class="contact-group">
        <div class="contact-row">
          <svg viewBox="0 0 10 10"><path d="M2 1 L4 1 L4.6 3 L3.4 3.8 Q4.4 5.8 6.2 6.6 L7 5.4 L9 6 L9 8 Q5 9.5 1 3 Z" fill="var(--gold)"/></svg>
          855.555.0142
        </div>
        <div class="contact-row">
          <svg viewBox="0 0 10 10"><rect x="2.5" y="0.5" width="5" height="9" rx="1" fill="none" stroke="var(--gold)" stroke-width="1.2"/></svg>
          973.555.0187
        </div>
      </div>
      <div class="contact-divider"></div>
      <div class="contact-group">
        <div class="contact-row">
          <svg viewBox="0 0 10 10"><rect x="0.5" y="2" width="9" height="6" fill="var(--gold)"/><path d="M0.5 2 L5 5.5 L9.5 2" fill="none" stroke="var(--navy)" stroke-width="0.9"/></svg>
          dana@ridgelinesawcutting.com
        </div>
        <div class="contact-row">
          <svg viewBox="0 0 10 10"><circle cx="5" cy="5" r="4.2" fill="none" stroke="var(--gold)" stroke-width="1.2"/><path d="M1 5 H9 M5 1 Q2.5 5 5 9 Q7.5 5 5 1" fill="none" stroke="var(--gold)" stroke-width="0.8"/></svg>
          www.ridgelinesawcutting.com
        </div>
      </div>
      <div class="contact-divider"></div>
      <div class="contact-group">
        <div>48 Quarry Ln.</div>
        <div>Fairview, NJ 07022</div>
      </div>
    </div>
  </section>

  <section class="card card-back">
    <div class="brand"><span class="brand-dot"></span>Ridgeline Sawcutting</div>
    <div class="hotline">855-CUTLINE</div>
    <div class="services">Wall Sawing<span class="sep">•</span>Core Drilling<span class="sep">•</span>Slab Sawing<span class="sep">•</span>Breaking &amp; Removal</div>
  </section>
</body>
</html>
```